Brindlecove Flood Restoration needing website

Hi Team

We are looking for a 4 or 5 page website containing
1: Home
2: Services
3: Gallery
4: Equipment Hire
5 Contact Us

Would want the front page to be a big call to action. Someones house has just flooded...they're highly stressed and we just want to let them know straight away that we can assist them

Some call to action would be great.

"Wet Carpets??"

"Washing machine just overflowed??"

"Burst pipe?"

"We're here to help!!"

Would be wanting a scrolling banner type homepage with images of flooded houses, heavy rain, a mother in shock that the house has been flooded by an overflowing washing machine, someone taking an emergency call with text saying that we are there to take your call 24/7 365 days a year

Target Market(s)

insurance companies and home owners

Industry/Entity Type

Hire

Coding

Coded - Design and coding required

Number of Pages Required

5+ page

Requirements
Must have
• 24/7 emergency contact number on home page (0498215763)
• 4 photos on banner on home page
• Equipment Hire Page should include images and brief description of these 3 products
• http://www.ptkdirect.example.com.au/prod458.htm
• http://www.gustline-gear.example.com.au/product/mistral-breeze-fan/
• http://www.vendrasuck.example.com.au/carpet/carpet-extractor-harrier-xv-x-vi-x-vii
• SERVICES OFFERED ARE:
• 24/7 Emergnecy Flood Restoration
• Insurance Claims
• Structural Drying
• Sub Floor Drying
• Supply and installation of drying equipment
• Professional Carpet and underlay installation
Nice to have
• Some other websites we like
• www.kelbyleakfixers.example.com.au
• www.summitrecoverywashing.example.com.au/flood-water-damage-restoration
• http://www.pelhamrecovery.example.com.au/
• http://www.dampfixnational.example.com.au/
Should not have
• not looking for an all white background.

```html
<!DOCTYPE html>
<html lang="en">
<head>
<meta charset="utf-8">
<title>Brindlecove Flood Restoration</title>
<link href="https://fonts.googleapis.com/css2?family=Raleway:wght@400;500;600;700;800&display=swap" rel="stylesheet">
<style>
:root{
  --nav-blue:#1d8fc8;
  --nav-blue-dark:#0f6fa6;
  --gold:#c9a648;
  --gold-light:#e8c766;
  --gold-dark:#6d5620;
  --welcome-a:#c9b48a;
  --welcome-b:#a88a56;
  --services-a:#3f4d63;
  --services-b:#2c3a4e;
  --gallery-a:#a68f47;
  --gallery-b:#7f6c33;
  --contact-a:#474d58;
  --contact-b:#2f343d;
  --ink:#ffffff;
  --card-title:#e9bd52;
  --field:#000000;
  --footer:#0b0b0b;
}
*{margin:0;padding:0;box-sizing:border-box}
html,body{width:1200px;height:2786px;overflow:hidden;background:#111}
body{font-family:"Raleway",sans-serif;color:var(--ink);position:relative}
.abs{position:absolute}
.section{position:absolute;left:0;width:1200px;overflow:hidden}

/* hero */
.hero{top:0;height:660px}
.hero-photo{position:absolute;inset:0;background:
  radial-gradient(ellipse 260px 160px at 275px 250px,rgba(255,214,120,.55),transparent 70%),
  radial-gradient(ellipse 260px 160px at 1000px 250px,rgba(255,214,120,.5),transparent 70%),
  linear-gradient(180deg,#6b4a2a 0%,#8a6a44 30%,#5a4d3f 55%,#242a2c 78%,#0e1112 100%)}
.nav-tab{position:absolute;left:0;top:0}
.main-nav{position:absolute;top:14px;left:0;width:1200px;display:flex;justify-content:center;gap:28px;font-size:13px;font-weight:600;letter-spacing:.3px}
.brand{position:absolute;top:552px;left:0;width:1200px;display:flex;justify-content:center;align-items:center;gap:14px}
.brand-mark{width:30px;height:30px;border-radius:50%;background:#2aa3dc}
.brand-name{font-size:30px;font-weight:700;color:#2aa3dc;letter-spacing:.5px}
.slide-arrow{position:absolute;top:573px}

.divider{position:absolute;left:0;width:1200px}

/* welcome */
.welcome{top:672px;height:362px}
.welcome-photo{position:absolute;inset:0;background:
  radial-gradient(ellipse 320px 200px at 600px 190px,rgba(150,120,70,.55),transparent 75%),
  linear-gradient(90deg,#8d7248 0%,var(--welcome-a) 22%,#b59a68 50%,var(--welcome-a) 78%,#d8cbb2 100%)}
.section-title{position:absolute;left:0;width:1200px;text-align:center;font-weight:800;letter-spacing:1px;text-shadow:0 2px 4px rgba(0,0,0,.25)}
.section-sub{position:absolute;left:0;width:1200px;text-align:center;font-size:10px;font-weight:700;letter-spacing:2.2px}
.welcome-copy{position:absolute;left:368px;width:464px;text-align:center;font-size:13.5px;line-height:18.5px;font-weight:500}
.welcome-copy p+p{margin-top:18px}

/* services */
.services{top:1040px;height:555px}
.services-photo{position:absolute;inset:0;background:
  radial-gradient(ellipse 420px 260px at 600px 300px,rgba(80,110,140,.35),transparent 75%),
  linear-gradient(180deg,#34404f 0%,var(--services-a) 45%,var(--services-b) 100%)}
.service-grid{position:absolute;left:234px;top:160px;width:732px;display:grid;grid-template-columns:repeat(3,1fr);gap:8px 6px}
.service-card{height:156px;border:1px solid rgba(255,255,255,.35);border-radius:12px;background:rgba(255,255,255,.05);text-align:center;padding:20px 18px 0}
.service-card h3{font-size:12.5px;font-weight:600;color:var(--card-title);line-height:15px;height:32px}
.service-card p{font-size:9px;line-height:11.5px;color:rgba(255,255,255,.85);height:48px}
.read-more{display:inline-block;margin-top:10px;width:78px;height:20px;line-height:18px;border:1px solid rgba(255,255,255,.7);border-radius:10px;font-size:7.5px;font-weight:700;letter-spacing:.5px}

/* gallery */
.gallery{top:1606px;height:640px}
.gallery-photo{position:absolute;inset:0;background:
  radial-gradient(ellipse 500px 300px at 600px 320px,rgba(190,170,100,.35),transparent 75%),
  linear-gradient(180deg,var(--gallery-a) 0%,#9a8440 55%,var(--gallery-b) 100%)}
.tile{position:absolute}
.gallery-nav{position:absolute;top:580px;left:569px;display:flex;gap:8px}
.gallery-nav span{width:22px;height:22px;border:1.5px solid rgba(255,255,255,.85);border-radius:50%;display:flex;align-items:center;justify-content:center}

/* contact */
.contact{top:2258px;height:479px}
.contact-photo{position:absolute;inset:0;background:
  radial-gradient(ellipse 500px 240px at 600px 320px,rgba(90,100,115,.4),transparent 75%),
  linear-gradient(180deg,var(--contact-a) 0%,#3d434d 50%,var(--contact-b) 100%)}
.contact-info{position:absolute;top:50px;left:234px;width:732px;display:grid;grid-template-columns:repeat(3,1fr);text-align:center}
.info-icon{width:44px;height:44px;border-radius:50%;background:#fff;margin:0 auto;display:flex;align-items:center;justify-content:center}
.info-label{margin-top:14px;font-size:12.5px;font-weight:500;letter-spacing:.5px}
.info-value{margin-top:8px;font-size:13px;font-weight:500}
.field{position:absolute;background:var(--field);border:1.5px solid #e6e6e6;font-size:9.5px;padding:11px 12px;color:#ddd;font-weight:500}
.send-btn{position:absolute;left:526px;top:395px;width:148px;height:45px;background:#a98d52;border:2px solid #f1e3bd;font-size:13px;font-weight:700;display:flex;align-items:center;justify-content:center}

.site-footer{position:absolute;top:2737px;left:0;width:1200px;height:49px;background:var(--footer);font-size:9px;font-weight:500}
.site-footer .copy{position:absolute;left:234px;top:20px}
</style>
</head>
<body>

<header class="section hero">
  <div class="hero-photo" role="img" aria-label="Photograph of a flooded living room at dusk with a sofa, floor lamps and a bicycle standing in water"></div>
  <svg class="nav-tab" width="1200" height="70" viewBox="0 0 1200 70">
    <path d="M150 0 H1050 C1000 40 820 56 600 56 C380 56 200 40 150 0 Z" fill="var(--nav-blue)"/>
    <path d="M150 0 C200 40 380 56 600 56 C820 56 1000 40 1050 0" fill="none" stroke="var(--gold-light)" stroke-width="3"/>
  </svg>
  <nav class="main-nav">
    <span>HOME</span><span>SERVICES</span><span>GALLERY</span><span>EQUIPMENT HIRE</span><span>CONTACT US</span>
  </nav>
  <div class="brand">
    <span class="brand-mark"></span>
    <span class="brand-name">Brindlecove Flood Restoration</span>
  </div>
  <svg class="slide-arrow" style="left:49px" width="28" height="28" viewBox="0 0 28 28"><circle cx="14" cy="14" r="13" fill="#c9a648"/><path d="M16 8 L10 14 L16 20" fill="none" stroke="#2a2a2a" stroke-width="3"/></svg>
  <svg class="slide-arrow" style="left:1123px" width="28" height="28" viewBox="0 0 28 28"><circle cx="14" cy="14" r="13" fill="#c9a648"/><path d="M12 8 L18 14 L12 20" fill="none" stroke="#2a2a2a" stroke-width="3"/></svg>
</header>

<svg class="divider" style="top:650px" width="1200" height="36" viewBox="0 0 1200 36">
  <path d="M0 10 C400 0 800 0 1200 10 V28 C800 20 400 20 0 28 Z" fill="var(--gold)"/>
  <path d="M0 14 C400 6 800 6 1200 14" fill="none" stroke="var(--gold-light)" stroke-width="2"/>
</svg>

<section class="section welcome">
  <div class="welcome-photo" role="img" aria-label="Photograph of a bright interior with a staircase and a white sofa"></div>
  <h1 class="section-title" style="top:52px;font-size:46px">WELCOME!</h1>
  <div class="section-sub" style="top:108px">TO BRINDLECOVE FLOOD RESTORATION</div>
  <div class="welcome-copy" style="top:140px">
    <p>Lorem ipsum dolor sit amet, usu id volumus insolens. Nec ad adipisci principes, eum omnes quaerendum at. Mel civibus nominavi suscipiantur cu, ne laudem senserit referrentur sea. Et enim libris scripta nam.</p>
    <p>Nullam facilis ex eum. His laoreet feugait et, postea consulatu et vim. Aliquid pericula ex sea, in eum natum fabulas commune. Te falli viris ignota eam, eos petentium reformidans in, lorem volutpat in ius. Nec ut nulla liber assentior, cu zril audiam ius. An sit legere salutatus definitionem, quo ex commodo aliquando.</p>
  </div>
</section>

<svg class="divider" style="top:1018px" width="1200" height="30" viewBox="0 0 1200 30">
  <path d="M0 4 C400 14 800 14 1200 4 V22 C800 30 400 30 0 22 Z" fill="#15161a"/>
  <path d="M0 20 C400 28 800 28 1200 20" fill="none" stroke="var(--gold)" stroke-width="3"/>
</svg>

<section class="section services">
  <div class="services-photo" role="img" aria-label="Photograph of a flooded room with furniture standing in water, tinted blue"></div>
  <h2 class="section-title" style="top:52px;font-size:44px">SERVICES</h2>
  <div class="section-sub" style="top:106px">BRINDLECOVE FLOOD RESTORATION</div>
  <div class="service-grid">
    <article class="service-card"><h3>24/7 Emergency Flood Restoration</h3><p>Lorem ipsum dolor sit amet, via melius fuisset omittantur ei, omittam petentium constituto ad eum, mallis ponderum ea mel. Cum at nonumes</p><span class="read-more">READ MORE</span></article>
    <article class="service-card"><h3>Insurance Claims</h3><p>Lorem ipsum dolor sit amet, via melius fuisset omittantur ei, omittam petentium constituto ad eum, mallis ponderum ea mel. Cum at nonumes</p><span class="read-more">READ MORE</span></article>
    <article class="service-card"><h3>Structural Drying</h3><p>Lorem ipsum dolor sit amet, via melius fuisset omittantur ei, omittam petentium constituto ad eum, mallis ponderum ea mel. Cum at nonumes</p><span class="read-more">READ MORE</span></article>
    <article class="service-card"><h3>Sub Floor Drying</h3><p>Lorem ipsum dolor sit amet, via melius fuisset omittantur ei, omittam petentium constituto ad eum, mallis ponderum ea mel. Cum at nonumes</p><span class="read-more">READ MORE</span></article>
    <article class="service-card"><h3>Supply and installation of drying equipment</h3><p>Lorem ipsum dolor sit amet, via melius fuisset omittantur ei, omittam petentium constituto ad eum, mallis ponderum ea mel. Cum at nonumes</p><span class="read-more">READ MORE</span></article>
    <article class="service-card"><h3>Professional Carpet and underlay installation</h3><p>Lorem ipsum dolor sit amet, via melius fuisset omittantur ei, omittam petentium constituto ad eum, mallis ponderum ea mel. Cum at nonumes</p><span class="read-more">READ MORE</span></article>
  </div>
</section>

<svg class="divider" style="top:1584px" width="1200" height="34" viewBox="0 0 1200 34">
  <path d="M0 6 C400 16 800 16 1200 6 V24 C800 14 400 14 0 24 Z" fill="var(--gold)"/>
  <path d="M0 24 C400 14 800 14 1200 24 V34 H0 Z" fill="#15161a"/>
</svg>

<section class="section gallery">
  <div class="gallery-photo" role="img" aria-label="Photograph of a flooded wooden interior with a chair and hanging shelves, tinted gold"></div>
  <h2 class="section-title" style="top:44px;font-size:50px">GALLERY</h2>
  <div class="section-sub" style="top:110px">BRINDLECOVE FLOOD RESTORATION</div>
  <div class="tile" style="left:234px;top:157px;width:171px;height:173px;background:linear-gradient(160deg,#2c302d,#1c1f1d)" role="img" aria-label="Dark photograph of a flooded room"></div>
  <svg class="abs" style="left:300px;top:224px" width="40" height="40" viewBox="0 0 40 40"><path d="M20 0 V40 M0 20 H40" stroke="rgba(255,255,255,.6)" stroke-width="1"/></svg>
  <div class="tile" style="left:405px;top:157px;width:310px;height:173px;background:linear-gradient(180deg,#8a7f86 0%,#9f9398 55%,#b9b3b0 100%)" role="img" aria-label="Photograph of a living room with a white sofa and a plant, floor covered in water"></div>
  <div class="tile" style="left:715px;top:157px;width:251px;height:173px;background:linear-gradient(180deg,#6c7072 0%,#8fa0a3 55%,#7fb4bb 100%)" role="img" aria-label="Photograph of a flooded dining and kitchen area"></div>
  <div class="tile" style="left:234px;top:330px;width:125px;height:215px;background:linear-gradient(180deg,#c8c6c0 0%,#9a7d63 60%,#8f9fa3 100%)" role="img" aria-label="Photograph of a flooded office with a floating toy duck"></div>
  <div class="tile" style="left:359px;top:330px;width:217px;height:215px;background:linear-gradient(180deg,#d9d6c8 0%,#b8b49c 55%,#8d8f80 100%)" role="img" aria-label="Photograph of a flooded bright room with an old television and furniture"></div>
  <div class="tile" style="left:576px;top:330px;width:390px;height:215px;background:radial-gradient(ellipse 80px 60px at 120px 70px,rgba(255,210,120,.6),transparent),linear-gradient(180deg,#6b4a2a 0%,#8a6a44 40%,#4d4a44 75%,#2a2d2e 100%)" role="img" aria-label="Photograph of a flooded living room at dusk with floor lamps"></div>
  <div class="gallery-nav">
    <span><svg width="8" height="10" viewBox="0 0 8 10"><path d="M6 1 L2 5 L6 9" fill="none" stroke="#fff" stroke-width="1.5"/></svg></span>
    <span><svg width="8" height="10" viewBox="0 0 8 10"><path d="M2 1 L6 5 L2 9" fill="none" stroke="#fff" stroke-width="1.5"/></svg></span>
  </div>
</section>

<svg class="divider" style="top:2232px" width="1200" height="34" viewBox="0 0 1200 34">
  <path d="M0 4 C400 14 800 14 1200 4 V22 C800 12 400 12 0 22 Z" fill="var(--gold)"/>
  <path d="M0 22 C400 12 800 12 1200 22 V32 C800 22 400 22 0 32 Z" fill="#15161a"/>
</svg>

<section class="section contact">
  <div class="contact-photo" role="img" aria-label="Photograph of a flooded living room, tinted dark grey"></div>
  <div class="contact-info">
    <div>
      <div class="info-icon"><svg width="20" height="20" viewBox="0 0 20 20"><path d="M10 2 L19 10 H16 V18 H12 V13 H8 V18 H4 V10 H1 Z" fill="#333"/></svg></div>
      <div class="info-label">ADDRESS</div>
      <div class="info-value">Harbourview Lane 17, Tarrowby</div>
    </div>
    <div>
      <div class="info-icon"><svg width="20" height="20" viewBox="0 0 20 20"><path d="M10 3 C15 3 18 6 18 9.5 C18 13 15 16 10 16 C9 16 8 15.8 7 15.5 L3 18 L4 14 C2.8 12.8 2 11.2 2 9.5 C2 6 5 3 10 3 Z" fill="#333"/></svg></div>
      <div class="info-label">MAIL</div>
      <div class="info-value">info@brindlecove.example.com</div>
    </div>
    <div>
      <div class="info-icon"><svg width="20" height="20" viewBox="0 0 20 20"><path d="M5 2 L8 2 L9 6 L7 8 C8 10.5 9.5 12 12 13 L14 11 L18 12 V15 C18 16.5 17 18 15 18 C8 17.5 2.5 12 2 5 C2 3 3.5 2 5 2 Z" fill="#333"/></svg></div>
      <div class="info-label">PHONE</div>
      <div class="info-value">0498215763</div>
    </div>
  </div>
  <div class="field" style="left:234px;top:183px;width:231px;height:41px">Enter Name</div>
  <div class="field" style="left:485px;top:183px;width:230px;height:41px">Enter Mail</div>
  <div class="field" style="left:734px;top:183px;width:232px;height:41px">Enter Subject</div>
  <div class="field" style="left:234px;top:243px;width:732px;height:134px">Enter Message</div>
  <div class="send-btn">Send Message</div>
</section>

<footer class="site-footer">
  <span class="copy">© Copyright 2016 <b>Brindlecove</b>. All Rights Reserved.</span>
</footer>

</body>
</html>
```